Business cards

We need business cards for the logo that you designed for our company. Something simple and clean.

Target Market(s)

Homeowners/ people looking for construction work

Industry/Entity Type

Construction

Contact Information for Business Card

Name: Doug Whitby, Number: 602-555-0174, Email: WhitbyBuildingCompany@mailbox-example.net ROC# 482063

Font styles to use
Serif

Colors

Designer to choose colors to be used in the design.

Requirements
Must have
• On one side of the card I would like to be all of the personal information I have put above along with the company logo that I have attached.
• On the other side of the card I would like the top half of the card to be the logo and then on the bottom half I would like to have the areas of construction we focus on along with an icon that represents it like the picture I have attached.
• Areas we focus on:
• Roofing, Kitchen and bath Remodel, Water Damage, Storm Damage, Fire Damage, Insurance Specialist
• If we could arrange those in alphabetical order.
Nice to have
• I have added 2 company logos a colorful one and a black one it would be nice to see a couple different options the black logo to be more simple and sleek and the colorful logo to be more colorful

```html
<!DOCTYPE html>
<html lang="en">
<head>
<meta charset="utf-8">
<title>Whitby Building Company – Business Cards</title>
<link rel="stylesheet" href="https://fonts.googleapis.com/css2?family=Lato:wght@400;700;900&family=Tinos&display=swap">
<style>
  :root {
    --stage: #3a3a3a;
    --sky: #35a8da;
    --brand-blue: #2fa3d8;
    --brand-red: #e8232b;
    --paper: #ffffff;
    --ink: #1b1b1b;
    --ink-soft: #1f2a33;
    --pin-green: #7ab648;
    --pin-face: #eef3e6;
    --rule-green: #2e8a3c;
  }
  * { box-sizing: border-box; margin: 0; padding: 0; }
  html, body { width: 1200px; height: 750px; overflow: hidden; }
  body { background: var(--stage); position: relative; font-family: "Tinos", serif; }

  .card { position: absolute; left: 367px; width: 467px; height: 266px; overflow: hidden; }
  .card--front { top: 93px; background: var(--sky); }
  .card--back { top: 406px; background: var(--paper); }

  .brand { position: absolute; display: flex; align-items: center; gap: 10px;
           font-family: "Lato", sans-serif; font-weight: 900; letter-spacing: 0.5px; white-space: nowrap; }
  .brand__mark { width: 20px; height: 20px; flex: none; }
  .card--front .brand { top: 48px; left: 0; right: 0; justify-content: center; font-size: 25px; color: var(--paper); }
  .card--front .brand__mark { background: var(--paper); }
  .card--back .brand { top: 54px; left: 24px; font-size: 22px; color: var(--brand-blue); }
  .card--back .brand__mark { background: var(--brand-blue); }

  .services { position: absolute; top: 117px; left: 0; width: 100%; height: 80px; }
  .service { position: absolute; width: 90px; margin-left: -45px; text-align: center;
             font-family: "Lato", sans-serif; color: var(--ink-soft); }
  .service svg { display: block; margin: 0 auto; width: 34px; height: 40px; }
  .service__title { font-weight: 900; font-size: 10px; line-height: 11px; margin-top: 9px; }
  .service__sub { font-size: 8px; line-height: 10px; letter-spacing: 0.2px; }
  .service--active::after { content: ""; position: absolute; left: 8px; right: 8px; top: 69px;
                            height: 2px; background: var(--rule-green); }

  .focus-list { position: absolute; top: 201px; left: 0; width: 100%; text-align: center;
                font-size: 12px; line-height: 15px; color: var(--ink-soft); }

  .band { position: absolute; bottom: 0; height: 8px; }
  .band--red-half { left: 0; width: 50%; background: var(--brand-red); }
  .band--white-half { right: 0; width: 50%; background: var(--paper); }
  .band--red-base { left: 0; width: 292px; height: 12px; background: var(--brand-red); }

  .contact { position: absolute; left: 25px; top: 150px; color: var(--ink); }
  .contact__name { font-family: "Lato", sans-serif; font-weight: 700; font-size: 15px; line-height: 15px; color: var(--brand-blue); }
  .contact__role { font-size: 12px; line-height: 13px; }
  .contact__list { list-style: none; margin-top: 12px; font-size: 12px; line-height: 15.5px; }
  .contact__list li { display: flex; align-items: center; gap: 7px; }
  .contact__list svg { width: 10px; height: 10px; flex: none; }
  .contact__roc { margin-top: 2px; }
</style>
</head>
<body>

<section class="card card--front" aria-label="Business card front">
  <div class="brand"><span class="brand__mark"></span>Whitby Building Company</div>

  <div class="services">
    <div class="service" style="left:74px">
      <svg viewBox="0 0 34 40" aria-hidden="true">
        <path d="M17 39C12 31 3 25 3 16a14 14 0 0 1 28 0c0 9-9 15-14 23z" fill="var(--pin-green)"/>
        <circle cx="17" cy="16" r="11" fill="var(--pin-face)"/>
        <path d="M17 8c3 5 6 8 6 11a6 6 0 0 1-12 0c0-3 3-6 6-11z" fill="#2f4fa6"/>
      </svg>
      <div class="service__title">WATER</div><div class="service__sub">DAMAGE</div>
    </div>
    <div class="service service--active" style="left:146px">
      <svg viewBox="0 0 34 40" aria-hidden="true">
        <path d="M17 39C12 31 3 25 3 16a14 14 0 0 1 28 0c0 9-9 15-14 23z" fill="var(--pin-green)"/>
        <circle cx="17" cy="16" r="11" fill="var(--pin-face)"/>
        <path d="M17 7c1 4 6 6 6 12a6 6 0 0 1-12 0c0-3 2-4 3-6 0 2 1 3 2 3 0-4 0-6 1-9z" fill="#d9272e"/>
      </svg>
      <div class="service__title">FIRE</div><div class="service__sub">DAMAGE</div>
    </div>
    <div class="service" style="left:222px">
      <svg viewBox="0 0 34 40" aria-hidden="true">
        <path d="M17 39C12 31 3 25 3 16a14 14 0 0 1 28 0c0 9-9 15-14 23z" fill="var(--pin-green)"/>
        <circle cx="17" cy="16" r="11" fill="var(--pin-face)"/>
        <g fill="#3d6b2a"><circle cx="13" cy="12" r="2"/><circle cx="19" cy="11" r="2"/><circle cx="16" cy="16" r="2"/><circle cx="21" cy="17" r="2"/><circle cx="13" cy="19" r="2"/><circle cx="18" cy="22" r="2"/></g>
      </svg>
      <div class="service__title">MOLD</div><div class="service__sub">REMEDIATION</div>
    </div>
    <div class="service" style="left:299px">
      <svg viewBox="0 0 34 40" aria-hidden="true">
        <path d="M17 39C12 31 3 25 3 16a14 14 0 0 1 28 0c0 9-9 15-14 23z" fill="var(--pin-green)"/>
        <circle cx="17" cy="16" r="11" fill="var(--pin-face)"/>
        <path d="M11 19a4 4 0 0 1 1-8 5 5 0 0 1 9 0 4 4 0 0 1 1 8z" fill="#6d7a86"/>
        <path d="M17 17l-2 4h3l-2 4" stroke="#f2c417" stroke-width="1.5" fill="none"/>
      </svg>
      <div class="service__title">STORM</div><div class="service__sub">DAMAGE</div>
    </div>
    <div class="service" style="left:377px">
      <svg viewBox="0 0 34 40" aria-hidden="true">
        <path d="M17 39C12 31 3 25 3 16a14 14 0 0 1 28 0c0 9-9 15-14 23z" fill="var(--pin-green)"/>
        <circle cx="17" cy="16" r="11" fill="var(--pin-face)"/>
        <rect x="10" y="9" width="14" height="14" fill="#f08a24"/>
        <g fill="#fff"><rect x="12" y="11" width="2" height="2"/><rect x="16" y="11" width="2" height="2"/><rect x="20" y="11" width="2" height="2"/><rect x="12" y="15" width="2" height="2"/><rect x="16" y="15" width="2" height="2"/><rect x="20" y="15" width="2" height="2"/></g>
      </svg>
      <div class="service__title">COMMERCIAL</div><div class="service__sub">SERVICES</div>
    </div>
  </div>

  <p class="focus-list">Roofing | Kitchen and bath Remodel | Water Damage | Storm Damage<br>Fire Damage | Insurance Specialist</p>

  <span class="band band--red-half"></span>
  <span class="band band--white-half"></span>
</section>

<section class="card card--back" aria-label="Business card back">
  <div class="brand"><span class="brand__mark"></span>Whitby Building Company</div>

  <div class="contact">
    <p class="contact__name">Doug Whitby</p>
    <p class="contact__role">Executive Assistant</p>
    <ul class="contact__list">
      <li>
        <svg viewBox="0 0 10 10" aria-hidden="true"><rect x="2" y="0.5" width="6" height="9" rx="1" fill="none" stroke="var(--brand-red)" stroke-width="1.2"/><rect x="4" y="7.3" width="2" height="1" fill="var(--brand-red)"/></svg>
        602-555-0174
      </li>
      <li>
        <svg viewBox="0 0 10 10" aria-hidden="true"><rect x="0.5" y="1.5" width="9" height="7" fill="var(--brand-red)"/><path d="M0.5 1.5l4.5 4 4.5-4M0.5 8.5l3.5-3.5M9.5 8.5L6 5" stroke="#fff" stroke-width="0.8" fill="none"/></svg>
        WhitbyBuildingCompany@mailbox-example.net
      </li>
      <li class="contact__roc">ROC# 482063</li>
    </ul>
  </div>

  <span class="band band--red-base"></span>
</section>

</body>
</html>
```